New shirt company looking for a fun and edgy online retail website design

We're a new company looking for a simple yet attractive website to sell shirts/tops to a mostly younger female audience. Our name is Tavi Shirt Co. and the PlanHerd logo is uploaded. We're thinking a home page, three separate pages for our shirt "collections", and a contact page/cart page for a grand total of 5 pages. We'd like the website to be coded, easy for the consumer to navigate/shop/checkout, and easy to link to various social media platforms and online websites. For colors, we're aiming for various blues, light grey, and maybe tan/khaki. Our goal is to launch with approximately 20-30 tops/shirts (or 7-10) per page. Please let us know if you have any questions and thank you for helping us! We are very excited to see what is created!

Target Market(s)

Female teens to early twenties

Coding

Coded - Design and coding required

Number of Pages Required

3 page

Font styles to use
Decorative
Script

Colors
cee9f5
85cae6
33a6d7
0393ce
cfdfed
85acd3

Requirements
Must have
• Online shopping/purchasing capabilities, dropdowns to select sizes for each item, easy to add/remove new or seasoned items.

```html
<!DOCTYPE html>
<html lang="en">
<head>
<meta charset="utf-8">
<title>Tavi Shirt Co. — Home</title>
<link rel="stylesheet" href="https://fonts.googleapis.com/css2?family=Montserrat:ital,wght@0,400;0,500;0,600;0,700;1,400&display=swap">
<style>
:root{
  --topbar:#38a3d6;
  --navbar:#a8dbf0;
  --hero-a:#7fcbe8;
  --hero-b:#2ea3d3;
  --brand:#0e8fd0;
  --brand-dark:#1a6fb5;
  --ink:#1d1d1d;
  --text:#444;
  --line:#b9b9b9;
  --studio:#ececec;
  --footer:#2b2b2b;
  --white:#fff;
}
*{box-sizing:border-box;margin:0;padding:0}
html,body{width:1200px;height:3407px;overflow:hidden}
body{position:relative;background:var(--white);font-family:"Montserrat",Arial,sans-serif;color:var(--text)}
.abs{position:absolute}
svg{display:block}

/* top bar */
.topbar{left:0;top:0;width:1200px;height:45px;background:var(--topbar);color:var(--white);font-size:9.5px;font-weight:600;text-transform:uppercase}
.topbar .currency{position:absolute;left:144px;top:17px}
.topbar .shipping{position:absolute;left:0;top:17px;width:1200px;text-align:center}
.topbar .cart{position:absolute;right:144px;top:17px;display:flex;gap:14px}

/* nav */
.navbar{left:0;top:45px;width:1200px;height:93px;background:var(--navbar);font-size:13.5px;text-transform:uppercase;color:#222}
.navbar a{position:absolute;top:37px;color:inherit;text-decoration:none}
.navbar .home{left:134px;top:32px;padding:4px 9px;border:1px solid #3a7fc0}
.logo{position:absolute;left:516px;top:12px;width:168px;height:66px;border:2px solid var(--brand-dark);display:flex;flex-direction:column;align-items:center;justify-content:center;color:var(--brand-dark);font-weight:600}
.logo .name{font-size:22px;letter-spacing:1px}
.logo .tag{font-size:9.5px;letter-spacing:2.5px;margin-top:2px}
.search{position:absolute;left:939px;top:29px;width:117px;height:33px;background:var(--white);font-size:10px;color:#555;padding:11px 13px}
.search svg{position:absolute;right:11px;top:11px}

/* hero */
.hero{left:0;top:138px;width:1200px;height:535px;background:radial-gradient(ellipse at 70% 35%,#b3e3f3 0%,var(--hero-a) 45%,var(--hero-b) 100%);overflow:hidden}
.hero-photo{position:absolute;left:120px;top:0;width:360px;height:535px;background:
  radial-gradient(ellipse 38% 22% at 50% 82%,rgba(227,180,36,.75) 0%,rgba(227,180,36,0) 100%),
  radial-gradient(ellipse 42% 40% at 50% 45%,rgba(205,218,206,.7) 0%,rgba(205,218,206,0) 100%)}
.hero-frame{position:absolute;left:492px;top:150px;width:564px;height:205px;border:3px solid #2b8fd0}
.hero-title{position:absolute;left:492px;top:200px;width:564px;text-align:center;font-size:64px;font-weight:500;color:#111;letter-spacing:1px}
.hero-btn{position:absolute;left:668px;top:325px;width:212px;height:61px;background:#2f9fd6;color:var(--white);font-size:21px;text-transform:uppercase;display:flex;align-items:center;justify-content:center}
.dots{position:absolute;left:1121px;top:243px;display:flex;flex-direction:column;gap:10px}
.dots i{width:9px;height:9px;border-radius:50%;background:var(--white)}
.dots i.on{background:#1f8fd0}

.section-title{left:0;width:1200px;text-align:center;font-size:28px;font-weight:400;color:var(--ink);text-transform:uppercase}

/* photo placeholders: studio backdrop with soft tone of the garment */
.ph{background:radial-gradient(ellipse 55% 45% at 50% 100%,var(--tone) 0%,var(--tone) 35%,rgba(255,255,255,0) 100%),var(--bg,var(--studio))}

/* products */
.products{left:144px;top:833px;display:grid;grid-template-columns:repeat(4,212px);column-gap:21px;row-gap:34px}
.product{width:212px;text-align:center}
.product .photo{height:190px}
.product .name{margin-top:26px;height:18px;font-size:13.5px;font-weight:500;color:#444;text-transform:uppercase}
.product .price{margin-top:12px;height:24px;font-size:20px;font-weight:600;color:#111}
.product .stars{margin-top:4px;height:16px;display:flex;justify-content:center;gap:5px}
.product .actions{margin-top:15px;display:flex;gap:12px;padding-left:8px}
.add{width:142px;height:40px;border:1.5px solid var(--line);color:var(--brand);font-size:14px;font-weight:700;text-transform:uppercase;display:flex;align-items:center;justify-content:center}
.add.active{background:var(--brand);border-color:var(--brand);color:var(--white)}
.wish{width:42px;height:40px;border:1.5px solid var(--line);display:flex;align-items:center;justify-content:center}

/* video */
.video{left:144px;top:1655px;width:912px;height:448px;color:var(--white);text-align:center;background:
  radial-gradient(ellipse 22% 45% at 62% 60%,rgba(236,232,226,.55) 0%,rgba(236,232,226,0) 100%),
  radial-gradient(ellipse 30% 55% at 63% 75%,rgba(125,82,52,.8) 0%,rgba(125,82,52,0) 100%),
  linear-gradient(90deg,#6d6e6a 0%,#8a8780 40%,#85776c 65%,#7c7e80 100%)}
.video h2{position:absolute;left:0;top:113px;width:100%;font-size:37px;font-weight:600}
.video p{position:absolute;left:0;top:174px;width:100%;font-size:19.5px;font-weight:500;text-transform:uppercase}
.video svg{position:absolute;left:411px;top:227px}

/* news */
.news{left:144px;top:2229px;display:flex;gap:20px}
.news-card{width:291px;height:401px;border:1px solid #e4e4e4;text-align:center}
.news-card .photo{height:213px}
.news-card h3{margin-top:27px;font-size:13px;font-weight:500;color:#555;text-transform:uppercase}
.news-card .date{margin-top:15px;font-size:13px;font-style:italic;color:#2a8fcf;display:flex;justify-content:center;gap:6px;align-items:center}
.news-card p{margin:12px 16px 0;font-size:11.5px;line-height:24px;color:#777}

/* instagram */
.insta{left:144px;top:2748px;display:flex;gap:13px}
.insta div{width:172px;height:164px}

/* footer */
.footer{left:0;top:3000px;width:1200px;height:407px;background:var(--footer);color:#ddd}
.footer h4{position:absolute;top:64px;font-size:14px;font-weight:700;color:var(--white);text-transform:uppercase}
.footer ul{position:absolute;top:98px;list-style:none;font-size:11.5px;line-height:24px}
.footer li{padding-left:25px;position:relative}
.links li::before{content:"";position:absolute;left:2px;top:9px;border-left:5px solid #ddd;border-top:3.5px solid transparent;border-bottom:3.5px solid transparent}
.contact li{padding-left:27px;line-height:27px;font-size:11px}
.contact li svg{position:absolute;left:0;top:8px}
.contact u{color:#fff}
.newsletter p{position:absolute;left:830px;top:99px;font-size:11.5px}
.newsletter .field{position:absolute;left:830px;top:138px;width:172px;height:45px;background:var(--white);color:#888;font-size:11px;padding:16px 19px}
.newsletter .send{position:absolute;left:1002px;top:138px;width:53px;height:45px;background:#1e8fd3;display:flex;align-items:center;justify-content:center}
.social{position:absolute;left:144px;top:330px;display:flex;gap:8px}
.social i{width:33px;height:33px;border:1.5px solid #eee;border-radius:50%}
.pay{position:absolute;left:441px;top:336px;display:flex;gap:5px}
.pay i{width:38px;height:23px;border-radius:2px}
.copy{position:absolute;right:145px;top:340px;font-size:11.5px;color:#eee}
</style>
</head>
<body>
<svg width="0" height="0" style="position:absolute">
  <defs>
    <symbol id="star" viewBox="0 0 20 20"><path d="M10 1l2.6 6 6.4.5-4.9 4.2 1.5 6.3L10 14.6 4.4 18l1.5-6.3L1 7.5l6.4-.5z" fill="#f2b400"/></symbol>
    <symbol id="star-half" viewBox="0 0 20 20"><path d="M10 1l2.6 6 6.4.5-4.9 4.2 1.5 6.3L10 14.6 4.4 18l1.5-6.3L1 7.5l6.4-.5z" fill="none" stroke="#f2b400" stroke-width="1.6"/><path d="M10 1v13.6L4.4 18l1.5-6.3L1 7.5l6.4-.5z" fill="#f2b400"/></symbol>
    <symbol id="heart" viewBox="0 0 24 24"><path d="M12 20s-8-5-8-11a4.5 4.5 0 0 1 8-2.8A4.5 4.5 0 0 1 20 9c0 6-8 11-8 11z" fill="none" stroke="#1a8bd0" stroke-width="1.8"/></symbol>
    <symbol id="cal" viewBox="0 0 12 12"><rect x="1" y="2" width="10" height="9" fill="none" stroke="#2a8fcf"/><path d="M1 5h10M4 1v2M8 1v2" stroke="#2a8fcf"/></symbol>
  </defs>
</svg>

<header>
  <div class="abs topbar">
    <span class="currency">Select currency USD &nbsp; ▾</span>
    <span class="shipping">Free shipping for orders over $60 (AUS) and $100 (US, UK, NZ).</span>
    <span class="cart"><span>Cart (0)</span><span>|</span><span>Checkout</span></span>
  </div>
  <nav class="abs navbar">
    <a class="home" href="#">Home</a>
    <a href="#" style="left:221px">Collections</a>
    <a href="#" style="left:351px">Contact</a>
    <div class="logo"><span class="name">TAVI</span><span class="tag">SHIRT COMPANY</span></div>
    <a href="#" style="left:786px">About</a>
    <a href="#" style="left:868px">News</a>
    <div class="search">SEARCH
      <svg width="11" height="11" viewBox="0 0 12 12"><circle cx="5" cy="5" r="3.8" fill="none" stroke="#444" stroke-width="1.6"/><path d="M8 8l3 3" stroke="#444" stroke-width="1.8"/></svg>
    </div>
  </nav>
</header>

<section class="abs hero">
  <div class="hero-photo" role="img" aria-label="Smiling woman in a pale green shirt and yellow trousers, arms crossed"></div>
  <div class="hero-frame"></div>
  <h1 class="hero-title">TAVI SHIRT CO</h1>
  <div class="hero-btn">Shop now</div>
  <div class="dots"><i></i><i class="on"></i><i></i></div>
</section>

<h2 class="abs section-title" style="top:745px">Featured Collections</h2>

<section class="abs products">
  <article class="product"><div class="photo ph" role="img" aria-label="Man in a red plaid shirt" style="--bg:#f3efeb;--tone:#9c3a3a"></div><div class="name">Product name here</div><div class="price">$245.00</div><div class="stars"><svg width="15" height="15"><use href="#star"/></svg><svg width="15" height="15"><use href="#star"/></svg><svg width="15" height="15"><use href="#star"/></svg><svg width="15" height="15"><use href="#star"/></svg><svg width="15" height="15"><use href="#star-half"/></svg></div><div class="actions"><div class="add active">Add to cart</div><div class="wish"><svg width="22" height="22"><use href="#heart"/></svg></div></div></article>
  <article class="product"><div class="photo ph" role="img" aria-label="Woman in a white shirt, arms crossed" style="--bg:#dcdcdc;--tone:#f6f6f6"></div><div class="name">Product name here</div><div class="price">$245.00</div><div class="stars"><svg width="15" height="15"><use href="#star"/></svg><svg width="15" height="15"><use href="#star"/></svg><svg width="15" height="15"><use href="#star"/></svg><svg width="15" height="15"><use href="#star"/></svg><svg width="15" height="15"><use href="#star-half"/></svg></div><div class="actions"><div class="add">Add to cart</div><div class="wish"><svg width="22" height="22"><use href="#heart"/></svg></div></div></article>
  <article class="product"><div class="photo ph" role="img" aria-label="Man in a navy shirt with glasses" style="--bg:#e4e4e4;--tone:#2f3b55"></div><div class="name">Product name here</div><div class="price">$245.00</div><div class="stars"><svg width="15" height="15"><use href="#star"/></svg><svg width="15" height="15"><use href="#star"/></svg><svg width="15" height="15"><use href="#star"/></svg><svg width="15" height="15"><use href="#star"/></svg><svg width="15" height="15"><use href="#star-half"/></svg></div><div class="actions"><div class="add">Add to cart</div><div class="wish"><svg width="22" height="22"><use href="#heart"/></svg></div></div></article>
  <article class="product"><div class="photo ph" role="img" aria-label="Woman in a light blue shirt with glasses" style="--bg:#e9e9e9;--tone:#d3ddee"></div><div class="name">Product name here</div><div class="price">$245.00</div><div class="stars"><svg width="15" height="15"><use href="#star"/></svg><svg width="15" height="15"><use href="#star"/></svg><svg width="15" height="15"><use href="#star"/></svg><svg width="15" height="15"><use href="#star"/></svg><svg width="15" height="15"><use href="#star-half"/></svg></div><div class="actions"><div class="add">Add to cart</div><div class="wish"><svg width="22" height="22"><use href="#heart"/></svg></div></div></article>
  <article class="product"><div class="photo ph" role="img" aria-label="Woman in a black and white striped shirt" style="--bg:#f3f3f3;--tone:#5a5a5a"></div><div class="name">Product name here</div><div class="price">$245.00</div><div class="stars"><svg width="15" height="15"><use href="#star"/></svg><svg width="15" height="15"><use href="#star"/></svg><svg width="15" height="15"><use href="#star"/></svg><svg width="15" height="15"><use href="#star"/></svg><svg width="15" height="15"><use href="#star-half"/></svg></div><div class="actions"><div class="add">Add to cart</div><div class="wish"><svg width="22" height="22"><use href="#heart"/></svg></div></div></article>
  <article class="product"><div class="photo ph" role="img" aria-label="Woman in a white shirt and jeans, seated" style="--bg:#f1f1f1;--tone:#35598c"></div><div class="name">Product name here</div><div class="price">$245.00</div><div class="stars"><svg width="15" height="15"><use href="#star"/></svg><svg width="15" height="15"><use href="#star"/></svg><svg width="15" height="15"><use href="#star"/></svg><svg width="15" height="15"><use href="#star"/></svg><svg width="15" height="15"><use href="#star-half"/></svg></div><div class="actions"><div class="add">Add to cart</div><div class="wish"><svg width="22" height="22"><use href="#heart"/></svg></div></div></article>
  <article class="product"><div class="photo ph" role="img" aria-label="Woman in a pale pink shirt, arms crossed" style="--bg:#f3f3f3;--tone:#ebd6de"></div><div class="name">Product name here</div><div class="price">$245.00</div><div class="stars"><svg width="15" height="15"><use href="#star"/></svg><svg width="15" height="15"><use href="#star"/></svg><svg width="15" height="15"><use href="#star"/></svg><svg width="15" height="15"><use href="#star"/></svg><svg width="15" height="15"><use href="#star-half"/></svg></div><div class="actions"><div class="add">Add to cart</div><div class="wish"><svg width="22" height="22"><use href="#heart"/></svg></div></div></article>
  <article class="product"><div class="photo ph" role="img" aria-label="Man in a white shirt and khaki trousers" style="--bg:#ececec;--tone:#c4ab88"></div><div class="name">Product name here</div><div class="price">$245.00</div><div class="stars"><svg width="15" height="15"><use href="#star"/></svg><svg width="15" height="15"><use href="#star"/></svg><svg width="15" height="15"><use href="#star"/></svg><svg width="15" height="15"><use href="#star"/></svg><svg width="15" height="15"><use href="#star-half"/></svg></div><div class="actions"><div class="add">Add to cart</div><div class="wish"><svg width="22" height="22"><use href="#heart"/></svg></div></div></article>
</section>

<section class="abs video" role="img" aria-label="Video still: woman in a white shirt and brown coat on a city bridge">
  <h2>SED UT PERSPICIATIS</h2>
  <p>Nemo enim ipsam voluptatem quia voluptas sit aspernatur</p>
  <svg width="90" height="90" viewBox="0 0 90 90"><circle cx="45" cy="45" r="43" fill="none" stroke="#fff" stroke-width="3"/><path d="M36 30v30l24-15z" fill="none" stroke="#fff" stroke-width="3" stroke-linejoin="round"/></svg>
</section>

<h2 class="abs section-title" style="top:2150px">Latest News</h2>

<section class="abs news">
  <article class="news-card"><div class="photo ph" role="img" aria-label="Bearded man in a plaid shirt with glasses" style="--bg:#e2e2e2;--tone:#4e6a90"></div><h3>Sed ut perspiciatis unde</h3><div class="date"><svg width="12" height="12"><use href="#cal"/></svg>JUNE 20, 2020</div><p>Nemo enim ipsam voluptatem quia voluptas sit aspernatur aut odit aut fugit, sed quia consequuntur mavoluptatem</p></article>
  <article class="news-card"><div class="photo ph" role="img" aria-label="Man in a straw hat and floral shirt on yellow" style="--bg:#f2b12b;--tone:#e8dcc4"></div><h3>Sed ut perspiciatis unde</h3><div class="date"><svg width="12" height="12"><use href="#cal"/></svg>JUNE 20, 2020</div><p>Nemo enim ipsam voluptatem quia voluptas sit aspernatur aut odit aut fugit, sed quia consequuntur mavoluptatem</p></article>
  <article class="news-card"><div class="photo ph" role="img" aria-label="Woman in a light blue shirt on grey" style="--bg:#8e8e8e;--tone:#c6daee"></div><h3>Sed ut perspiciatis unde</h3><div class="date"><svg width="12" height="12"><use href="#cal"/></svg>JUNE 20, 2020</div><p>Nemo enim ipsam voluptatem quia voluptas sit aspernatur aut odit aut fugit, sed quia consequuntur mavoluptatem</p></article>
</section>

<h2 class="abs section-title" style="top:2670px">Instagram</h2>

<section class="abs insta">
  <div class="ph" role="img" aria-label="Man in a blue shirt on a turquoise wall" style="--bg:#4cc3de;--tone:#7aa6d6"></div>
  <div class="ph" role="img" aria-label="Woman in a green shirt and yellow trousers" style="--bg:#55c3df;--tone:#d2c98f"></div>
  <div class="ph" role="img" aria-label="Folded polo and check shirts on white boards" style="--bg:#eef0f2;--tone:#6a7a9a"></div>
  <div class="ph" role="img" aria-label="Smiling woman holding a phone on blue" style="--bg:#48c6e4;--tone:#7f9fcb"></div>
  <div class="ph" role="img" aria-label="Shirts hanging on a clothes rail" style="--bg:#9aa8bc;--tone:#e3e9f2"></div>
</section>

<footer class="abs footer">
  <h4 style="left:146px">Contact us</h4>
  <ul class="contact" style="left:146px">
    <li><svg width="12" height="11" viewBox="0 0 12 11"><path d="M1 3c2-2 8-2 10 0v2H8V3.5H4V5H1z M2 6h8l1 4H1z" fill="#eee"/></svg>(000)-121-1231 (Phone)</li>
    <li><svg width="12" height="11" viewBox="0 0 12 11"><rect x="3" y="0" width="6" height="3" fill="#eee"/><rect x="0" y="3.5" width="12" height="5" fill="#eee"/><rect x="3" y="7" width="6" height="4" fill="#eee"/></svg>(000)-121-1231 &nbsp;(Fax)</li>
    <li><svg width="12" height="9" viewBox="0 0 12 9"><rect x=".5" y=".5" width="11" height="8" fill="none" stroke="#eee"/><path d="M.5.5L6 5l5.5-4.5" fill="none" stroke="#eee"/></svg><u>hello@tavishirt.example</u></li>
    <li style="line-height:13px;padding-top:7px"><svg width="10" height="13" viewBox="0 0 10 13"><path d="M5 12S1 7 1 4.5a4 4 0 0 1 8 0C9 7 5 12 5 12z" fill="none" stroke="#eee" stroke-width="1.4"/><circle cx="5" cy="4.5" r="1.3" fill="#eee"/></svg>#1452 Lorem Ipsum Dummy<br>Text Lorem Ipsum</li>
  </ul>

  <h4 style="left:376px">Information</h4>
  <ul class="links" style="left:376px">
    <li>Sitemap</li><li>Shipping &amp; Returns</li><li>Privacy Notice</li><li>Conditions of Use</li><li>About us</li><li>Contact us</li>
  </ul>

  <h4 style="left:590px">Customer service</h4>
  <ul class="links" style="left:590px">
    <li>Search</li><li>Blog</li><li>Recently viewed products</li><li>Compare products list</li><li>New products</li>
  </ul>

  <div class="newsletter">
    <h4 style="left:830px">Sign up newsletter</h4>
    <p>At vero eos et accusamus et iusto odio</p>
    <div class="field">Enter Your Email :</div>
    <div class="send"><svg width="20" height="18" viewBox="0 0 20 18"><path d="M1 8L19 1 13 17 9 10z" fill="#fff"/><path d="M9 10L19 1" stroke="#1e8fd3" stroke-width="1.2"/></svg></div>
  </div>

  <div class="social" aria-label="Social links"><i></i><i></i><i></i><i></i><i></i></div>
  <div class="pay" aria-label="Accepted payment methods"><i style="background:#2d6fb6"></i><i style="background:#d9892e"></i><i style="background:#5a9bd5"></i><i style="background:#e9e2d6"></i></div>
  <div class="copy">© Copyright 2020.Tavi Shirt Co .,All Rights Reserved &nbsp;| &nbsp;Privacy Policy</div>
</footer>
</body>
</html>
```